Modern Medical Optometry Website

We need mordern, Patient friendly website. Easy to navigate and enhance our advance medical technology and excellent patient care.
1. HOME PAGE
2. OUR TEAM PAGE
3. EYECARE PAGE - VISION SERVICES, EYE EXAMS, KERATOCONUS CENTER, GLAUCOMA , DIABITES, VELMORIN EXAM, DIGITAL RETINAL, OCT.
4. MYOPIA CONTROL CLINIC
5. DRY EYE CLINIC
6. EYEWEAR
7. PATIENT CENTER - BLOG
7. CONTACT US
This is our current website www.lumvarta.com
and We want to add more content and a cleaner design like these website
http://norvellbrookclinic.com/
https://www.tqvamori.com/

```html
<!DOCTYPE html>
<html lang="en">
<head>
<meta charset="utf-8">
<title>Lumvarta Optometry</title>
<link rel="stylesheet" href="https://fonts.googleapis.com/css2?family=Lato:wght@300;400;700&family=Oswald:wght@300;400&display=swap">
<style>
:root{
  --white:#ffffff;
  --page:#f4f4f4;
  --ink:#222222;
  --ink-soft:#555555;
  --accent-blue:#1b7fa6;
  --hero-a:#c9ccd6;
  --hero-b:#8d9ccc;
  --tile-yellow:#d8d86a;
  --tile-team:#c79f93;
  --tile-eyecare:#8ea5c2;
  --tile-myopia:#c5674a;
  --tile-dry:#7fa5cf;
  --tile-green:#5aaf5a;
  --hours-a:#3fd0c4;
  --hours-b:#4fb56a;
  --clients-bg:#d6dade;
  --write-a:#23606e;
  --write-b:#1b4a5c;
  --send:#2e8a6a;
  --footer:#2a2a2a;
  --gold:#e7b423;
}
*{box-sizing:border-box;margin:0;padding:0}
html,body{width:1200px;height:4569px;overflow:hidden}
body{background:var(--white);font-family:'Lato',sans-serif;color:var(--ink);position:relative}
.abs{position:absolute}

/* hero */
.hero{position:absolute;left:18px;top:24px;width:1164px;height:725px;overflow:hidden}
.hero-photo{position:absolute;inset:0;background:linear-gradient(90deg,var(--hero-a) 0%,#b3b9d0 40%,var(--hero-b) 100%)}
.topbar{position:absolute;left:0;top:0;width:1164px;height:80px;background:rgba(255,255,255,.92)}
.top-btn{position:absolute;top:8px;height:16px;background:#2f7e93;color:var(--white);font-size:8px;line-height:16px;text-align:center;letter-spacing:.5px}
.lang{position:absolute;right:30px;top:8px;width:70px;height:16px;border:1px solid #999;font-size:8px;line-height:14px;text-align:center;color:var(--ink-soft)}
.nav{position:absolute;top:44px;display:flex;gap:34px;font-size:12px;letter-spacing:.6px;color:#2a5e7a;font-weight:700}
.nav .active{border-bottom:2px solid var(--accent-blue);padding-bottom:4px}
.brand-box{position:absolute;left:530px;top:0;width:110px;height:116px;background:var(--white);display:flex;flex-direction:column;align-items:center;justify-content:center;gap:8px}
.brand-box .sq{width:30px;height:30px;background:var(--gold)}
.brand-box span{font-size:11px;font-weight:700;color:#333;letter-spacing:1px;text-align:center;line-height:1.3}
.hero-title{position:absolute;left:585px;top:180px;color:var(--white);font-family:'Lato',sans-serif;font-weight:700;font-size:60px;line-height:64px;letter-spacing:4px}
.hero-copy{position:absolute;left:585px;top:380px;width:380px;color:var(--white);font-size:15px;line-height:20px}
.hero-copy p+p{margin-top:14px}
.learn{position:absolute;left:585px;top:568px;padding:10px 22px;border:1px solid rgba(255,255,255,.7);color:var(--white);font-size:15px;letter-spacing:2px}
.dots{position:absolute;left:555px;top:676px;display:flex;gap:6px}
.dots i{width:10px;height:10px;border-radius:50%;border:1px solid var(--white);display:block}
.dots i:first-child{background:var(--white)}

/* statements */
.statement{position:absolute;left:0;width:1200px;height:336px;background:var(--page)}
.statement .bar{position:absolute;width:12px;background:var(--accent-blue)}
.statement .text{position:absolute;font-family:'Oswald',sans-serif;font-size:30px;line-height:44px;color:var(--ink);letter-spacing:.6px}
.statement .photo{position:absolute}

/* tiles */
.tile{position:absolute;overflow:hidden;color:var(--white)}
.tile h3{font-family:'Oswald',sans-serif;font-weight:300;font-size:32px;letter-spacing:2px;line-height:34px;text-transform:uppercase}
.tile p{font-size:14px;line-height:20px;margin-top:6px}
.tile .lead{font-family:'Oswald',sans-serif;font-weight:300;font-size:30px;line-height:44px}
.show{position:absolute;border:2px solid rgba(255,255,255,.8);color:var(--white);font-size:20px;letter-spacing:3px;text-align:center;line-height:52px;height:56px;width:180px}
.show.sm{width:110px;height:40px;line-height:36px;font-size:18px}

/* hours */
.hours{position:absolute;left:0;top:2157px;width:1200px;height:438px;background:linear-gradient(180deg,var(--hours-a) 0%,#3fc7a4 55%,var(--hours-b) 100%);color:var(--white);text-align:center}
.hours h2{position:absolute;width:100%;top:30px;font-weight:300;font-size:50px;letter-spacing:2px}
.hours-table{position:absolute;left:213px;top:149px;width:768px;height:64px;display:flex;border:2px solid rgba(255,255,255,.6)}
.hours-table div{flex:1;border-right:2px solid rgba(255,255,255,.6);font-size:15px;line-height:22px;padding-top:9px;background:rgba(255,255,255,.12)}
.hours-table div:last-child{border-right:0}
.hours-note{position:absolute;width:100%;top:272px;font-size:15px}
.cta{position:absolute;top:347px;height:56px;width:342px;border:2px solid rgba(255,255,255,.7);font-size:16px;letter-spacing:2px;line-height:52px;background:rgba(255,255,255,.08)}

/* clients */
.clients{position:absolute;left:0;top:2595px;width:1200px;height:603px}
.clients-bg{position:absolute;inset:0;background:radial-gradient(ellipse at 40% 60%,#9aa5ad 0%,var(--clients-bg) 45%,#e9ebec 100%)}
.clients h2{position:absolute;width:100%;top:28px;text-align:center;font-weight:300;font-size:52px;letter-spacing:2px;color:var(--ink)}
.clients-panel{position:absolute;left:228px;top:116px;width:747px;height:411px;background:rgba(255,255,255,.55)}
.quote{position:absolute;width:330px;display:flex;gap:16px}
.avatar{width:46px;height:46px;border-radius:50%;background:#c9c9c9;flex:none}
.quote p{font-size:12px;line-height:15px;font-style:italic;color:#444}
.quote h4{margin-top:10px;font-family:'Oswald',sans-serif;font-weight:400;font-size:20px;color:var(--ink)}
.quote small{font-size:12px;color:var(--ink-soft)}
.arrow{position:absolute;top:305px}

/* find us */
.find{position:absolute;left:0;top:3198px;width:1200px;height:634px}
.find-info{position:absolute;left:0;top:0;width:600px;height:634px;background:var(--white)}
.find-info h2{position:absolute;width:100%;top:28px;text-align:center;font-weight:400;font-size:52px;letter-spacing:1px}
.find-brand{position:absolute;left:200px;top:130px;width:210px;display:flex;flex-direction:column;align-items:center;gap:10px}
.find-brand .sq{width:70px;height:70px;background:var(--gold)}
.find-brand span{font-size:14px;font-weight:700;letter-spacing:2px;color:#333}
.address{position:absolute;left:238px;top:328px;font-size:14px;line-height:30px;color:#333;letter-spacing:.5px}
.map{position:absolute;left:600px;top:0;width:600px;height:634px;background:linear-gradient(135deg,#eceae6 0%,#e2e4e6 60%,#d9dde0 100%)}

/* write us */
.write{position:absolute;left:0;top:3832px;width:1200px;height:554px;background:linear-gradient(180deg,var(--write-a) 0%,var(--write-b) 100%);color:var(--white)}
.write h2{position:absolute;width:100%;top:42px;text-align:center;font-weight:300;font-size:50px;letter-spacing:3px}
.field{position:absolute;background:rgba(255,255,255,.1);font-size:14px;letter-spacing:2px;text-align:center;color:rgba(255,255,255,.8)}
.send{position:absolute;left:238px;top:386px;width:731px;height:52px;background:var(--send);text-align:center;line-height:52px;font-size:15px;font-weight:700;letter-spacing:3px}

/* footer */
.footer{position:absolute;left:0;top:4386px;width:1200px;height:183px;background:var(--footer);color:#cfcfcf;font-size:14px;letter-spacing:1px}
.footer-brand{position:absolute;left:230px;top:40px;width:110px;display:flex;flex-direction:column;align-items:center;gap:8px}
.footer-brand .sq{width:44px;height:44px;background:var(--gold)}
.footer-brand span{font-size:11px;font-weight:700;text-align:center;line-height:1.3;color:#cfcfcf}
.footer-col{position:absolute;top:36px;line-height:38px}
</style>
</head>
<body>

<section class="hero">
  <div class="hero-photo" role="img" aria-label="Photo of a smiling mother and daughter at an eye exam, with optometry equipment, under a soft blue overlay"></div>
  <header class="topbar">
    <div class="top-btn" style="left:12px;width:110px">818-555-0142 / CALL OR TEXT US</div>
    <div class="top-btn" style="left:130px;width:110px">REQUEST AN APPOINTMENT</div>
    <div class="lang">ENGLISH</div>
    <nav class="nav" style="left:22px">
      <span class="active">HOME</span><span>OUR TEAM</span><span>EYECARE</span><span>MYOPIA CONTROL CLINIC</span>
    </nav>
    <nav class="nav" style="left:710px">
      <span>DRY EYE CLINIC</span><span>EYEWEAR</span><span>PATIENT CENTER - BLOG</span><span>CONTACT US</span>
    </nav>
  </header>
  <div class="brand-box"><div class="sq"></div><span>LUMVARTA<br>OPTOMETRY</span></div>
  <h1 class="hero-title">THE<br>LUMVARTA<br>PROMISE</h1>
  <div class="hero-copy">
    <p>Welcome to Lumvarta Optometry, where your vision and eye health are our sole priority.</p>
    <p>We take great pride in providing you with state-of-the-art eyecare matched with personal attention from our staff and doctors.</p>
  </div>
  <div class="learn">LEARN MORE &#9656;</div>
  <div class="dots"><i></i><i></i><i></i><i></i><i></i></div>
</section>

<section class="statement" style="top:780px">
  <div class="bar" style="left:125px;top:97px;height:137px"></div>
  <p class="text" style="left:170px;top:96px">Your quality of life is our goal and we<br>believe that healthy eyesight is vital<br>to achieving it.</p>
  <div class="photo" role="img" aria-label="Photo of a woman at a desk rubbing her tired eyes, beside a potted plant" style="left:655px;top:0;width:497px;height:332px;background:linear-gradient(90deg,#f1f1ef 0%,#e4e4e2 55%,#bdbdbd 100%)"></div>
</section>

<section class="statement" style="top:1142px;background:var(--white)">
  <div class="photo" role="img" aria-label="Close-up photo of an eye and a contact lens on a fingertip" style="left:43px;top:0;width:490px;height:335px;background:linear-gradient(90deg,#d9c6c0 0%,#b79c94 50%,#eeeeee 100%)"></div>
  <p class="text" style="right:134px;top:96px;text-align:right">Our professional and personable staff<br>is highly trained in helping you achieve<br>and maintain healthy eyesight.</p>
  <div class="bar" style="left:1085px;top:98px;height:143px"></div>
</section>

<div class="tile" style="left:0;top:1502px;width:600px;height:329px;background:var(--tile-yellow)">
  <p class="lead abs" style="left:36px;top:56px">Your quality of life is our goal and<br>we believe that healthy eyesight<br>is vital to achieving it.</p>
  <div class="show" style="left:36px;top:226px">SHOW</div>
</div>
<div class="tile" role="img" aria-label="Our Team tile with a photo of an optometrist, tinted rose" style="left:600px;top:1502px;width:302px;height:329px;background:var(--tile-team)">
  <div class="abs" style="left:14px;top:22px;width:270px">
    <h3>Our Team</h3>
    <p>Meet our doctors and staff who care for every patient with skill and warmth.</p>
  </div>
  <div class="show sm" style="left:96px;top:256px">SHOW</div>
</div>
<div class="tile" role="img" aria-label="Eyecare tile with a photo of an eye exam, tinted blue" style="left:902px;top:1502px;width:298px;height:329px;background:var(--tile-eyecare)">
  <div class="abs" style="left:14px;top:22px;width:270px">
    <h3>Eyecare</h3>
    <p>Complete eye exams, retinal imaging and OCT scans using the latest clinical tools.</p>
  </div>
  <div class="show sm" style="left:94px;top:256px">SHOW</div>
</div>
<div class="tile" role="img" aria-label="Myopia Control Clinic tile with a photo of a child, tinted orange" style="left:0;top:1831px;width:300px;height:326px;background:var(--tile-myopia)">
  <div class="abs" style="left:14px;top:20px;width:272px">
    <h3>Myopia<br>Control<br>Clinic</h3>
    <p>Proven treatments that slow nearsightedness in growing children and protect future vision.</p>
  </div>
  <div class="show sm" style="left:90px;top:248px">SHOW</div>
</div>
<div class="tile" role="img" aria-label="Dry Eye Clinic tile with a photo of a person with dry eyes, tinted light blue" style="left:300px;top:1831px;width:300px;height:326px;background:var(--tile-dry)">
  <div class="abs" style="left:14px;top:20px;width:272px">
    <h3>Dry Eye Clinic</h3>
    <p>Relief for dry, tired eyes with tailored therapy and gentle in-office care.</p>
  </div>
  <div class="show sm" style="left:94px;top:248px">SHOW</div>
</div>
<div class="tile" style="left:600px;top:1831px;width:600px;height:326px;background:var(--tile-green)">
  <p class="lead abs" style="right:38px;top:56px;text-align:right">Your quality of life is our goal and<br>we believe that healthy eyesight<br>is vital to achieving it.</p>
  <div class="show" style="left:360px;top:222px">SHOW</div>
</div>

<section class="hours">
  <h2>Hours</h2>
  <div class="hours-table">
    <div>Monday - Thursday<br>9 am - 6 pm</div>
    <div>Friday<br>8:30 am - 5 pm</div>
    <div>Saturday<br>8:30 am - 3 pm</div>
    <div>Closed on<br>Sundays</div>
  </div>
  <p class="hours-note">Please keep in mind we are closed for lunch 1-2 pm</p>
  <div class="cta" style="left:238px">818-555-0142 / CALL OR TEXT US</div>
  <div class="cta" style="left:615px">MAKE AN APPOINTMENT</div>
</section>

<section class="clients">
  <div class="clients-bg" role="img" aria-label="Soft blurred background photo of a close-up eye"></div>
  <h2>Our Clients</h2>
  <div class="clients-panel"></div>
  <svg class="arrow" style="left:178px" width="22" height="40" viewBox="0 0 22 40"><path d="M18 4 L4 20 L18 36" fill="none" stroke="#666" stroke-width="4"/></svg>
  <svg class="arrow" style="left:990px" width="22" height="40" viewBox="0 0 22 40"><path d="M4 4 L18 20 L4 36" fill="none" stroke="#666" stroke-width="4"/></svg>
  <div class="quote" style="left:256px;top:168px"><div class="avatar"></div><div><p>"The whole team was friendly and patient. My exam was thorough and every question I had was answered clearly."</p><h4>MARA VOSS</h4><small>Patient</small></div></div>
  <div class="quote" style="left:600px;top:168px"><div class="avatar"></div><div><p>"Booking was easy and the doctor explained my results in plain words. I finally have glasses that feel right."</p><h4>THEO LIND</h4><small>Patient</small></div></div>
  <div class="quote" style="left:256px;top:360px"><div class="avatar"></div><div><p>"The whole team was friendly and patient. My exam was thorough and every question I had was answered clearly."</p><h4>MARA VOSS</h4><small>Patient</small></div></div>
  <div class="quote" style="left:600px;top:360px"><div class="avatar"></div><div><p>"Booking was easy and the doctor explained my results in plain words. I finally have glasses that feel right."</p><h4>THEO LIND</h4><small>Patient</small></div></div>
</section>

<section class="find">
  <div class="find-info">
    <h2>Find Us</h2>
    <div class="find-brand"><div class="sq"></div><span>LUMVARTA OPTOMETRY</span></div>
    <p class="address">LUMVARTA OPTOMETRY<br>4820 Calloway Ave,<br>Brennfield, CA 90417<br>Phone: 818-555-0142<br>Fax: 818-555-0178</p>
  </div>
  <div class="map" role="img" aria-label="Street map showing the clinic location with a marker"></div>
</section>

<section class="write">
  <h2>Write Us</h2>
  <div class="field" style="left:238px;top:164px;width:341px;height:50px;line-height:50px">YOUR NAME</div>
  <div class="field" style="left:624px;top:164px;width:345px;height:50px;line-height:50px">YOUR E-MAIL</div>
  <div class="field" style="left:238px;top:237px;width:731px;height:125px;padding-top:16px">YOUR MESSAGE</div>
  <div class="send">SEND</div>
</section>

<footer class="footer">
  <div class="footer-brand"><div class="sq"></div><span>LUMVARTA<br>OPTOMETRY</span></div>
  <div class="footer-col" style="left:503px">LUMVARTA OPTOMETRY<br>4820 Calloway Ave,<br>Brennfield, CA 90417</div>
  <div class="footer-col" style="left:810px">Phone: 818-555-0142<br>Fax: 818-555-0178</div>
</footer>

</body>
</html>
```